Business Card - Cooperate

Business Card for Larkfield Management Consulting

Target Market(s)

Corparte - b2B

Industry/Entity Type

Management Consulting - Professional Services

Contact Information for Business Card

Company Name , Slogan , Dummy Address,

Requirements
Must have
• Reach your Full Potential

```html
<!DOCTYPE html>
<html lang="en">
<head>
<meta charset="utf-8">
<title>Larkfield Management Consulting — Business Card</title>
<link href="https://fonts.googleapis.com/css2?family=Montserrat:wght@400;500;600;700&display=swap" rel="stylesheet">
<style>
  :root {
    --bg: #d9d9d7;
    --white: #ffffff;
    --navy: #2a2f86;
    --blue: #3a64b0;
    --green: #7cc242;
    --name-green: #6cbd3c;
    --ink: #3a3a3a;
    --muted: #b9bcc4;
    --black: #141414;
    --black-soft: #2a2a2a;
  }
  * { box-sizing: border-box; margin: 0; padding: 0; }
  html, body { width: 1200px; height: 801px; overflow: hidden; }
  body {
    background: var(--bg);
    font-family: "Montserrat", Arial, sans-serif;
    display: flex;
    align-items: center;
    justify-content: center;
    gap: 60px;
  }
  .card {
    position: relative;
    width: 520px;
    height: 297px;
    overflow: hidden;
    border-bottom: 4px solid var(--green);
  }

  /* Front */
  .card-front { background: var(--white); }
  .brand-name {
    font-weight: 600;
    font-size: 40px;
    line-height: 1;
    color: var(--blue);
    letter-spacing: 1px;
    white-space: nowrap;
  }
  .card-front .brand-name { position: absolute; left: 36px; top: 44px; }
  .person { position: absolute; left: 36px; top: 118px; }
  .person-name {
    font-weight: 700;
    font-size: 19px;
    color: var(--name-green);
    text-transform: uppercase;
    white-space: nowrap;
  }
  .person-title { font-size: 14px; color: var(--ink); margin-top: 2px; }
  .band {
    position: absolute;
    left: 0;
    right: 60px;
    top: 178px;
    bottom: 0;
    background: linear-gradient(90deg, var(--navy), var(--blue));
  }
  .band-circle {
    position: absolute;
    right: 22px;
    top: 118px;
    width: 100px;
    height: 100px;
    border-radius: 50%;
    border: 5px solid var(--white);
    background: var(--blue);
  }
  .contact {
    position: absolute;
    left: 36px;
    top: 190px;
    color: var(--white);
    font-size: 12.5px;
    line-height: 1.45;
    white-space: nowrap;
  }
  .contact-address { margin-bottom: 8px; }
  .contact-line { display: flex; align-items: center; gap: 7px; }
  .contact-line svg { width: 11px; height: 11px; flex: none; }

  /* Back */
  .card-back { background: var(--black); }
  .back-pattern {
    position: absolute;
    inset: 0;
    background: radial-gradient(ellipse at 70% 30%, var(--black-soft), var(--black) 70%);
  }
  .back-content {
    position: absolute;
    left: 50%;
    top: 50%;
    transform: translate(-50%, -50%);
    display: flex;
    flex-direction: column;
    align-items: center;
    gap: 18px;
  }
  .back-brand { display: flex; align-items: center; gap: 14px; }
  .back-dot {
    width: 40px;
    height: 40px;
    border-radius: 50%;
    background: var(--green);
  }
  .slogan {
    font-size: 13px;
    font-weight: 400;
    color: var(--muted);
    white-space: nowrap;
  }
</style>
</head>
<body>

  <section class="card card-front" aria-label="Business card front">
    <div class="brand-name">larkfield</div>

    <div class="person">
      <div class="person-name">Nolan Whitaker</div>
      <div class="person-title">Director</div>
    </div>

    <div class="band"></div>
    <div class="band-circle"></div>

    <div class="contact">
      <div class="contact-address">1187 Birchmont Lane<br>Salem, OR 97301</div>
      <div class="contact-line">
        <svg viewBox="0 0 12 12" aria-hidden="true"><path d="M2.5 1 L4.5 1 L5 3.5 L3.8 4.6 A6 6 0 0 0 7.4 8.2 L8.5 7 L11 7.5 L11 9.5 A1.5 1.5 0 0 1 9.5 11 A8.5 8.5 0 0 1 1 2.5 A1.5 1.5 0 0 1 2.5 1 Z" fill="#7cc242"/></svg>
        (555) 214-3086
      </div>
      <div class="contact-line">
        <svg viewBox="0 0 12 12" aria-hidden="true"><rect x="1" y="2.5" width="10" height="7" fill="none" stroke="#7cc242" stroke-width="1.2"/><path d="M1 2.5 L6 6.5 L11 2.5" fill="none" stroke="#7cc242" stroke-width="1.2"/></svg>
        info@larkfieldmc.com
      </div>
      <div class="contact-line">
        <svg viewBox="0 0 12 12" aria-hidden="true"><circle cx="6" cy="6" r="5" fill="#7cc242"/><path d="M1 6 H11 M6 1 V11" stroke="#2a2f86" stroke-width="0.8"/></svg>
        www.larkfieldmc.com
      </div>
    </div>
  </section>

  <section class="card card-back" aria-label="Business card back">
    <div class="back-pattern" role="img" aria-label="Glossy tonal repeating pattern on black"></div>
    <div class="back-content">
      <div class="back-brand">
        <div class="back-dot"></div>
        <div class="brand-name">larkfield</div>
      </div>
      <p class="slogan">Reach your full potential</p>
    </div>
  </section>

</body>
</html>
```